CD Cover Design Project

Project 2 CD cover design. One in English and one in Chinese. (I can provide the Chinese in PDF or any file if necessary.)
I will use the same design for 6 different CD cover with different title only. They all are related to my business-hypnosis.
I have Logo and the main content of the picture for you to design a cover.
I hope the whole design look like all while in a distance but only the title words show up. When you look closely you can see the design-the bird.
Will decide ASAP.
Target Market(s)
My students and audiences in hypnotist training courses.
Customer from my website and my hypnosis office.
Attendee in my lecture and conference.
Industry/Entity Type
Business
Requirements
Must have
- 1. It should looks close to white when been seen in a distance or first sight.
You can make my art work almost disappear or change to an idea like this Letter printing design.
Please visit:
http://plinkzap.example/images/pear_letterpress_macro.jpg
http://www.corvamid.example/wp-content/uploads/2007/02/letterpress_2.jpg
2.About my logo.
Please use only the Bird sign but not the rest of the name and address.
Please have this information about the publisher on the other side:
"Self-hypnosis for Relaxation"
p.s. You can change the size and font and colour any way you wish.
This will be the other side of the cover.
Thank you.
CD Cover ,back, contain information-
Self-hypnosis for Relaxation
Benefits about Self hypnosis. You can fall back to sleep so much easier every night! Keeps a sense of logic and ease of mind every day. It gives you the control of your emotions and situations. You can apply it on daily business.
To help yourself to go into the deeper hypnotic trance easily you need to five yourself permission to dream, fantasize and play before allowing your rational mind to do the necessary job of sorting, assessing and figuring out hot to act upon the information that you receive. Many of us rationalize or criticize too quickly, without giving our intuition the time and space it deserve.
To give your self permission to use your imagination constructively and to open your mind and emotions to a newer ability, here are some suggestions for you to use. They are simple but powerful positive affirmations that gently help to alter your beliefs, habits and expectation toward your foal. When used on a regular basis is that they will help to make you more available for some experiences and less available for others. The power of this self-hypnosis is strong: what we ask for, we often receive.
Lie down with your back fully supported or sit comfortable in a quiet place.
Relax and breathe easily and deeply. Every time you breathe out, you feel more relaxed.
Count from 10 to 1, at each count you feel even more relax. At the last count, hold your breath and count for 3 seconds then let go, breathe out.
Read in your mind 10 times the following statement. In order not to full asleep, move your fingers while counting from the right hand to the left.
I’m calm. I’m relax. I’m in control.
ADD LOGO HERE
Fern Trance
www.ferntrance.example Ontario, Canada (555) 246-3187
- end -
Nice to have
- Clean and quiet, spiritual.
This is my both English and Chinese website. Please check it out even you might not read Chinese. All of the picture and art works are done by myself.
www.ferntrance.example
www.tw.ferntrance.example

```html
<!DOCTYPE html>
<html lang="en">
<head>
<meta charset="utf-8">
<title>Good night sleep – CD cover</title>
<link href="https://fonts.googleapis.com/css2?family=Archivo+Narrow:ital,wght@0,400;1,400&family=Oswald:wght@300&display=swap" rel="stylesheet">
<style>
  :root {
    --backdrop: #ecebe6;
    --stone: #c9c6bc;
    --stone-light: #d8d5cc;
    --stone-dark: #b3afa3;
    --card: #f7f3dc;
    --ink: #55534b;
    --ink-soft: #6c695f;
    --tab: #e2df8e;
    --tab-dark: #b9b562;
    --logo: #1c1c1c;
  }
  * { box-sizing: border-box; margin: 0; padding: 0; }
  html, body { width: 1200px; height: 1000px; overflow: hidden; }
  body {
    background: var(--backdrop);
    font-family: "Archivo Narrow", "Arial Narrow", sans-serif;
    color: var(--ink);
    position: relative;
  }
  .cover {
    position: absolute;
    width: 480px; height: 480px;
    top: 260px;
    box-shadow: 0 6px 18px rgba(0,0,0,.18);
    overflow: hidden;
  }
  .cover--back { left: 50px; }
  .cover--front { left: 560px; }
  .cover__art {
    position: absolute; inset: 0;
    background: radial-gradient(ellipse at 45% 55%, var(--stone-light) 0%, var(--stone) 60%, var(--stone-dark) 100%);
  }
  .info-card {
    position: absolute;
    top: 0; left: 20px;
    width: 430px; height: 380px;
    background: var(--card);
    border-radius: 0 0 22px 22px;
    box-shadow: 0 4px 10px rgba(0,0,0,.25);
    padding: 22px 22px 16px 26px;
    font-size: 8.6px;
    line-height: 1.28;
  }
  .info-card__tab {
    position: absolute; top: 0; right: -18px;
    width: 18px; height: 120px;
    background: var(--stone-dark);
    border-radius: 0 0 6px 0;
  }
  .info-card h1 { font-size: 9.5px; font-weight: 400; margin-bottom: 9px; }
  .info-card p { margin-bottom: 2px; }
  .info-card .affirmation { font-style: italic; margin-top: 10px; }
  .publisher {
    position: absolute; left: 20px; bottom: 16px;
    font-size: 8px; line-height: 1.3; color: var(--ink-soft);
  }
  .title-tab {
    position: absolute; top: 42px; right: 0;
    width: 200px; height: 40px;
    background: linear-gradient(180deg, var(--tab) 0%, #d6d27c 100%);
    border-radius: 8px 0 0 8px;
    box-shadow: 0 2px 4px rgba(0,0,0,.25);
    display: flex; align-items: center; padding-left: 14px;
    font-family: "Oswald", "Arial Narrow", sans-serif;
    font-weight: 300; font-size: 24px; color: #4a4834;
  }
  .brand {
    position: absolute; left: 22px; bottom: 22px;
    display: flex; align-items: center; gap: 6px;
    font-size: 11px; color: var(--logo); letter-spacing: .04em;
  }
  .brand__dot { width: 14px; height: 14px; border-radius: 50%; background: var(--logo); }
  .spine {
    position: absolute; left: 1090px; top: 260px;
    width: 18px; height: 480px;
    background: var(--card);
    box-shadow: 0 0 0 2px var(--stone);
    display: flex; align-items: center; justify-content: center;
  }
  .spine span {
    writing-mode: vertical-rl;
    font-size: 9px; letter-spacing: .05em; color: var(--ink);
  }
</style>
</head>
<body>

<section class="cover cover--back">
  <div class="cover__art" role="img" aria-label="Faint embossed letterpress bird artwork on grey textured stock"></div>
  <div class="info-card">
    <div class="info-card__tab"></div>
    <h1>Self-hypnosis for Relaxation</h1>
    <p>Benefits about Self hypnosis. You can fall back to sleep so much easier every night! Keeps a sense of logic and ease of mind every day. It gives you the control of your emotions and situations. You can apply it on daily business.</p>
    <p>To help yourself to go into the deeper hypnotic trance easily you need to five yourself permission to dream, fantasize and play before allowing your rational mind to do the necessary job of sorting, assessing and figuring out hot to act upon the information that you receive. Many of us rationalize or criticize too quickly, without giving our intuition the time and space it deserve.</p>
    <p>To give your self permission to use your imagination constructively and to open your mind and emotions to a newer ability, here are some suggestions for you to use. They are simple but powerful positive affirmations that gently help to alter your beliefs, habits and expectation toward your foal. When used on a regular basis is that they will help to make you more available for some experiences and less available for others. The power of this self-hypnosis is strong: what we ask for, we often receive.</p>
    <p>Lie down with your back fully supported or sit comfortable in a quiet place.</p>
    <p>Relax and breathe easily and deeply. Every time you breathe out, you feel more relaxed.</p>
    <p>Count from 10 to 1, at each count you feel even more relax. At the last count, hold your breath and count for 3 seconds then let go, breathe out.</p>
    <p>Read in your mind 10 times the following statement. In order not to full asleep, move your fingers while counting from the right hand to the left.</p>
    <p class="affirmation">I’m calm. &nbsp;I’m relax. &nbsp;I’m in control.</p>
    <p>Fern Trance</p>
    <p>www.ferntrance.example &nbsp;Ontario, Canada (555) 246-3187</p>
  </div>
  <div class="publisher">
    FT-RLX0001001<br>
    Published by Fern Trance<br>
    48 Willowmere Rd, Suite 5, Brookdale, ON K0X 1A0<br>
    (555)246-3187<br>
    www.ferntrance.example
  </div>
</section>

<section class="cover cover--front">
  <div class="cover__art" role="img" aria-label="Large embossed letterpress bird artwork, white on grey textured stock"></div>
  <div class="title-tab">Good night sleep</div>
  <div class="brand"><span class="brand__dot"></span>FERN TRANCE</div>
</section>

<aside class="spine"><span>GOOD NIGHT SLEEP</span></aside>

</body>
</html>
```